PowerPoint Template Design for business consulting company in Silicon Valley

I need a PowerPoint template to use as the starting point for new presentations. I have a logo but now need design that supports this. I've attached a very descriptive PDF that explains exactly what I need. Here is a list of deliverables: 1. PowerPoint Template that I will use as the starter presentation for all new Lantern Quorix presentationsDesigns for the following slides: See picture below for examples of structure:2. Title slide with subtitle3. Section header4. Title and body5. Title and 2 columns6. Title and 3 columns7. One column text8. Editable timeline to show months, or steps for a process9. Bullet design for unordered list (can be graphic)10. Bullet design for ordered list11. Recommended fonts for each design: Title, subtitle, list, captionOPTIONAL: Possible graphic elements to be used for section title slide backgrounds or graphic elements:--Your team / my team / people on project--Goals for project / presentation--Editable Timeline--Speaking--Writing--Listening--People collaborating / helping each otherI am happy to accept proposals for developing these optional elements in a separate project.

Requirements
Must have
• Must be FLAT design.
• Not flashy or garish. Must be subtle.

```html
<!DOCTYPE html>
<html lang="en">
<head>
<meta charset="utf-8">
<title>Lantern Quorix – Presentation Template</title>
<link rel="stylesheet" href="https://fonts.googleapis.com/css2?family=Arimo:wght@400;700&family=Marcellus&family=Cardo:wght@400;700&display=swap">
<style>
:root{
  --blue:#1650a0;
  --blue-dark:#0f3f86;
  --blue-light:#3d8fe0;
  --green:#1a7a3a;
  --ink:#1c1c1c;
  --grey-bg:#5a5a5a;
  --stage:#f1f1f1;
  --footer:#ececec;
  --track:#f3ede4;
  --white:#ffffff;
}
*{box-sizing:border-box;margin:0;padding:0}
html,body{width:1200px;height:2643px;overflow:hidden}
body{background:var(--grey-bg);font-family:"Cardo",serif;color:var(--ink);position:relative}
.stage{position:absolute;left:0;top:0;width:1200px;height:805px;background:var(--stage)}
.hero{position:absolute;left:247px;top:204px;transform:scale(1.3);transform-origin:0 0;box-shadow:0 6px 24px rgba(0,0,0,.18)}
.slide{position:absolute;width:543px;height:305px;background:var(--white);overflow:hidden}
.slide svg.bg{position:absolute;left:0;top:0}
.col-l{left:48px}.col-r{left:633px}
.row1{top:863px}.row2{top:1221px}.row3{top:1577px}.row4{top:1929px}.row5{top:2287px}
.abs{position:absolute}
.bar-top-green{position:absolute;left:0;top:0;width:505px;height:6px;background:var(--green)}
.bar-top-blue{position:absolute;left:505px;top:0;width:38px;height:8px;background:var(--blue-dark)}
.footer{position:absolute;left:0;bottom:0;width:543px;height:20px;background:var(--footer)}
.footer-url{position:absolute;left:210px;bottom:6px;font-family:"Arimo",sans-serif;font-size:6.5px;letter-spacing:2px;color:#555}
.page-no{position:absolute;right:14px;bottom:4px;width:15px;height:15px;border-radius:50%;background:var(--green);color:var(--white);font-family:"Arimo",sans-serif;font-size:7px;display:flex;align-items:center;justify-content:center}
.heading{position:absolute;left:0;top:14px;width:100%;text-align:center;font-family:"Marcellus",serif;font-size:14px;color:var(--ink);letter-spacing:.3px}
.heading .accent{color:var(--green)}
.year-tab{position:absolute;left:201px;top:0;width:141px;height:36px;background:var(--white);clip-path:polygon(0 0,100% 0,100% 75%,50% 100%,0 75%);color:var(--blue);font-family:"Arimo",sans-serif;font-weight:700;font-size:20px;text-align:center;line-height:32px}
.main-title{position:absolute;left:0;top:60px;width:100%;text-align:center;color:var(--white);font-family:"Arimo",sans-serif;font-weight:700;font-size:25px}
.brand-disc{position:absolute;width:108px;height:108px;border-radius:50%;background:var(--white);display:flex;align-items:center;justify-content:center;text-align:center;font-family:"Arimo",sans-serif;font-weight:700;font-size:16px;line-height:1.1;color:var(--blue)}
.body-sm{font-size:7px;line-height:1.45;color:#333}
.toc{position:absolute;left:270px;top:52px;width:260px}
.toc-row{display:flex;align-items:center;height:28px;font-family:"Arimo",sans-serif;font-size:7px;color:#333}
.toc-row .leader{flex:1;border-bottom:1px dashed #999;margin:0 6px}
.photo{position:absolute}
.box-label{position:absolute;background:var(--blue);color:var(--white);font-family:"Cardo",serif;font-size:8px;display:flex;align-items:center;justify-content:center}
.side-note{position:absolute;text-align:right;width:190px}
.center-note{position:absolute;text-align:center;width:120px}
.step-note{position:absolute;text-align:center;width:110px}
.progress{position:absolute;left:257px;width:238px;height:12px;border-radius:6px;background:var(--track)}
.progress i{display:block;height:100%;border-radius:6px;background:var(--blue)}
.value{position:absolute;left:505px;width:22px;height:12px;border-radius:6px;background:var(--green);color:var(--white);font-family:"Arimo",sans-serif;font-size:6.5px;text-align:center;line-height:12px}
.contact-bar{position:absolute;left:0;bottom:0;width:543px;height:34px;background:var(--blue);display:flex;justify-content:space-around;align-items:center;color:var(--white);font-family:"Arimo",sans-serif;font-size:7px}
.contact-bar span{display:flex;align-items:center;gap:4px}
.brand-mark{position:absolute;left:784px;top:2326px;width:238px;height:176px;display:flex;align-items:center;justify-content:center;text-align:center;color:var(--white);font-family:"Arimo",sans-serif;font-weight:700;font-size:36px;line-height:1.1}
</style>
</head>
<body>

<section class="stage">
  <div class="slide hero">
    <svg class="bg" width="543" height="305" viewBox="0 0 543 305">
      <defs><linearGradient id="sky0" x1="0" y1="0" x2="0" y2="1"><stop offset="0" stop-color="#a9c9ec"/><stop offset="1" stop-color="#2d4f8c"/></linearGradient></defs>
      <rect width="543" height="305" fill="url(#sky0)" role="img" aria-label="Photo of glass office towers against a blue sky"/>
      <polygon points="0,0 543,0 543,100 271.5,175 0,100" fill="var(--blue)"/>
      <polygon points="0,100 271.5,175 543,100 543,113 271.5,188 0,113" fill="var(--green)"/>
    </svg>
    <div class="year-tab">2018</div>
    <div class="main-title">PRESENTATION TITLE GOES HERE</div>
    <div class="brand-disc" style="left:217px;top:103px">Lantern<br>Quorix</div>
  </div>
</section>

<!-- Title slide -->
<div class="slide col-l row1">
  <svg class="bg" width="543" height="305" viewBox="0 0 543 305">
    <defs><linearGradient id="sky1" x1="0" y1="0" x2="0" y2="1"><stop offset="0" stop-color="#a9c9ec"/><stop offset="1" stop-color="#2d4f8c"/></linearGradient></defs>
    <rect width="543" height="305" fill="url(#sky1)" role="img" aria-label="Photo of glass office towers against a blue sky"/>
    <polygon points="0,0 543,0 543,100 271.5,175 0,100" fill="var(--blue)"/>
    <polygon points="0,100 271.5,175 543,100 543,113 271.5,188 0,113" fill="var(--green)"/>
  </svg>
  <div class="year-tab">2018</div>
  <div class="main-title">PRESENTATION TITLE GOES HERE</div>
  <div class="brand-disc" style="left:217px;top:103px">Lantern<br>Quorix</div>
</div>

<!-- Contents slide -->
<div class="slide col-r row1">
  <svg class="bg" width="543" height="305" viewBox="0 0 543 305">
    <defs><linearGradient id="desk" x1="0" y1="0" x2="1" y2="1"><stop offset="0" stop-color="#6b5444"/><stop offset="1" stop-color="#2e2a2a"/></linearGradient></defs>
    <polygon points="0,0 190,0 230,141 190,285 0,285" fill="url(#desk)" role="img" aria-label="Photo of a business handshake over a desk with a laptop"/>
    <polyline points="205,0 245,141 205,285" fill="none" stroke="var(--green)" stroke-width="7"/>
  </svg>
  <div class="bar-top-green" style="left:230px;width:275px"></div><div class="bar-top-blue"></div>
  <div class="toc">
    <div class="toc-row">Title Goes Here<span class="leader"></span>03</div>
    <div class="toc-row">Title Goes Here<span class="leader"></span>04</div>
    <div class="toc-row">Title Goes Here<span class="leader"></span>05</div>
    <div class="toc-row">Title Goes Here<span class="leader"></span>06</div>
    <div class="toc-row">Title Goes Here<span class="leader"></span>07</div>
    <div class="toc-row">Title Goes Here<span class="leader"></span>08</div>
    <div class="toc-row">Title Goes Here<span class="leader"></span>09</div>
  </div>
  <div class="footer"></div><div class="footer-url">www.webaddress.com</div><div class="page-no">2</div>
</div>

<!-- Section header -->
<div class="slide col-l row2">
  <svg class="bg" width="543" height="305" viewBox="0 0 543 305">
    <defs><linearGradient id="faded" x1="0" y1="0" x2="1" y2="1"><stop offset="0" stop-color="#e4e4e4"/><stop offset="1" stop-color="#f6f6f6"/></linearGradient></defs>
    <rect width="543" height="305" fill="url(#faded)" role="img" aria-label="Faded photo of a desk with documents"/>
    <polygon points="0,0 543,0 543,45 271.5,112 0,45" fill="var(--blue)"/>
    <polygon points="0,45 271.5,112 543,45 543,57 271.5,124 0,57" fill="var(--green)"/>
    <circle cx="271.5" cy="53" r="16" fill="none" stroke="#fff" stroke-width="1.2"/>
    <text x="271.5" y="58" text-anchor="middle" fill="#fff" font-family="Arimo, sans-serif" font-size="13">01</text>
    <circle cx="271.5" cy="241" r="9" fill="var(--blue)"/>
    <path d="M271.5 236v9M267.5 241.5l4 4 4-4" stroke="#fff" stroke-width="1.5" fill="none"/>
  </svg>
  <div class="heading" style="top:165px;font-size:24px">LOREM IPSUM <span class="accent">SIMPLY TEXT</span></div>
  <div class="footer" style="background:#e9e9e9"></div><div class="footer-url">www.webaddress.com</div><div class="page-no">3</div>
</div>

<!-- Title and body -->
<div class="slide col-r row2">
  <div class="bar-top-green"></div><div class="bar-top-blue"></div>
  <div class="heading">LOREM IPSUM <span class="accent">SIMPLY TEXT</span></div>
  <div class="abs" style="left:0;top:100px;width:543px;height:115px;background:var(--blue)"></div>
  <div class="photo" style="left:16px;top:68px;width:162px;height:185px;background:linear-gradient(160deg,#a7c46a,#6e7f3c 55%,#b79a6a)" role="img" aria-label="Photo of a glass jar of coins beside a growing plant"></div>
  <p class="abs body-sm" style="left:198px;top:114px;width:325px;color:#fff;font-size:7.5px">Lorem Ipsum is simply dummy text of the printing and typesetting industry. Lorem Ipsum has been the industry's standard dummy text ever since the 1500s, when an unknown printer took a galley of type and scrambled it to make a type specimen book. It has survived not only five centuries, but also the leap into electronic typesetting, remaining essentially unchanged.</p>
  <div class="footer"></div><div class="footer-url">www.webaddress.com</div><div class="page-no">4</div>
</div>

<!-- Three columns -->
<div class="slide col-l row3">
  <div class="bar-top-green"></div><div class="bar-top-blue"></div>
  <div class="heading">LOREM IPSUM <span class="accent">SIMPLY TEXT</span></div>
  <svg class="bg" width="543" height="305" viewBox="0 0 543 305">
    <g id="donut">
      <circle cx="76" cy="123" r="45" fill="none" stroke="var(--blue-light)" stroke-width="20"/>
      <path d="M76 78 A45 45 0 1 0 121 123" fill="none" stroke="var(--blue)" stroke-width="20"/>
      <circle cx="76" cy="123" r="22" fill="#fff"/>
      <circle cx="76" cy="118" r="5" fill="var(--blue)"/><path d="M67 132a9 8 0 0 1 18 0z" fill="var(--blue)"/>
    </g>
    <use href="#donut" x="197"/><use href="#donut" x="393"/>
  </svg>
  <p class="center-note body-sm" style="left:16px;top:200px">Lorem Ipsum is simply dummy text of the printing and typesetting industry.</p>
  <p class="center-note body-sm" style="left:213px;top:200px">Lorem Ipsum is simply dummy text of the printing and typesetting industry.</p>
  <p class="center-note body-sm" style="left:409px;top:200px">Lorem Ipsum is simply dummy text of the printing and typesetting industry.</p>
  <div class="footer"></div><div class="footer-url">www.webaddress.com</div><div class="page-no">5</div>
</div>

<!-- Hub diagram -->
<div class="slide col-r row3">
  <div class="bar-top-green"></div><div class="bar-top-blue"></div>
  <div class="heading">LOREM IPSUM <span class="accent">SIMPLY TEXT</span></div>
  <svg class="bg" width="543" height="305" viewBox="0 0 543 305">
    <polyline points="384,79 495,79 495,130" fill="none" stroke="var(--blue)" stroke-width="1.2"/>
    <line x1="331" y1="165" x2="410" y2="165" stroke="var(--blue)" stroke-width="1.2"/>
    <polyline points="416,244 495,244 495,205" fill="none" stroke="var(--blue)" stroke-width="1.2"/>
    <circle cx="460" cy="167" r="42" fill="none" stroke="var(--blue-light)" stroke-width="14"/>
    <path d="M460 125 A42 42 0 1 1 418 167" fill="none" stroke="var(--blue)" stroke-width="14"/>
  </svg>
  <div class="abs" style="left:430px;top:148px;width:60px;text-align:center;font-family:'Arimo',sans-serif;font-weight:700;font-size:9px;line-height:1.1;color:var(--blue)">Lantern<br>Quorix</div>
  <div class="box-label" style="left:287px;top:65px;width:97px;height:28px">LOREM IPSUM</div>
  <div class="box-label" style="left:236px;top:151px;width:95px;height:29px">LOREM IPSUM</div>
  <div class="box-label" style="left:321px;top:230px;width:95px;height:29px">LOREM IPSUM</div>
  <p class="side-note body-sm" style="left:88px;top:68px">Lorem Ipsum is simply dummy text of the printing and typesetting industry Lorem Ipsum.</p>
  <p class="side-note body-sm" style="left:37px;top:154px">Lorem Ipsum is simply dummy text of the printing and typesetting industry Lorem Ipsum.</p>
  <p class="side-note body-sm" style="left:122px;top:233px">Lorem Ipsum is simply dummy text of the printing and typesetting industry Lorem Ipsum.</p>
  <div class="footer"></div><div class="footer-url">www.webaddress.com</div><div class="page-no">6</div>
</div>

<!-- Process steps -->
<div class="slide col-l row4">
  <div class="bar-top-green"></div><div class="bar-top-blue"></div>
  <div class="heading">LOREM IPSUM <span class="accent">SIMPLY TEXT</span></div>
  <svg class="bg" width="543" height="305" viewBox="0 0 543 305">
    <g fill="var(--blue)">
      <polygon points="16,105 136,105 150,131 136,157 16,157"/>
      <polygon points="142,105 266,105 280,131 266,157 142,157 156,131"/>
      <polygon points="272,105 396,105 410,131 396,157 272,157 286,131"/>
      <polygon points="402,105 520,105 534,131 520,157 402,157 416,131"/>
    </g>
    <g fill="#fff">
      <circle cx="78" cy="126" r="5"/><path d="M69 141a9 8 0 0 1 18 0z"/>
      <circle cx="213" cy="126" r="5"/><path d="M204 141a9 8 0 0 1 18 0z"/>
      <circle cx="343" cy="126" r="5"/><path d="M334 141a9 8 0 0 1 18 0z"/>
      <circle cx="473" cy="126" r="5"/><path d="M464 141a9 8 0 0 1 18 0z"/>
    </g>
    <g fill="var(--green)" stroke="#fff" stroke-width="2">
      <circle cx="30" cy="131" r="14"/><circle cx="160" cy="131" r="14"/><circle cx="290" cy="131" r="14"/><circle cx="420" cy="131" r="14"/>
    </g>
    <g fill="#fff" font-family="Arimo, sans-serif" font-weight="700" font-size="13" text-anchor="middle">
      <text x="30" y="136">A</text><text x="160" y="136">B</text><text x="290" y="136">C</text><text x="420" y="136">D</text>
    </g>
  </svg>
  <p class="step-note body-sm" style="left:30px;top:182px">Lorem Ipsum is simply dummy text of the printing and typesetting industry.</p>
  <p class="step-note body-sm" style="left:158px;top:182px">Lorem Ipsum is simply dummy text of the printing and typesetting industry.</p>
  <p class="step-note body-sm" style="left:288px;top:182px">Lorem Ipsum is simply dummy text of the printing and typesetting industry.</p>
  <p class="step-note body-sm" style="left:416px;top:182px">Lorem Ipsum is simply dummy text of the printing and typesetting industry.</p>
  <div class="footer"></div><div class="footer-url">www.webaddress.com</div><div class="page-no">7</div>
</div>

<!-- Progress bars -->
<div class="slide col-r row4">
  <div class="bar-top-green"></div><div class="bar-top-blue"></div>
  <div class="heading">LOREM IPSUM <span class="accent">SIMPLY TEXT</span></div>
  <div class="photo" style="left:14px;top:85px;width:197px;height:73px;background:linear-gradient(120deg,#8ea0ad,#d9dde0 60%,#a9b3ba)" role="img" aria-label="Photo of colleagues reviewing documents at a desk"></div>
  <div class="abs" style="left:14px;top:162px;width:197px;height:14px;background:var(--green);color:#fff;font-family:'Cardo',serif;font-size:6.5px;text-align:center;line-height:14px">LOREM IPSUM IS SIMPLY DUMMY TEXT</div>
  <p class="abs body-sm" style="left:14px;top:176px;width:197px;height:49px;padding:5px 14px;background:#e8eef8;text-align:center;font-size:6.5px">Lorem Ipsum is simply dummy text of the printing and typesetting industry. Lorem Ipsum has been the industry's standard dummy text ever since the 1500s.</p>
  <div class="progress" style="top:102px"><i style="width:24%"></i></div><div class="value" style="top:102px">30</div>
  <div class="progress" style="top:141px"><i style="width:82%"></i></div><div class="value" style="top:141px">85</div>
  <div class="progress" style="top:178px"><i style="width:14%"></i></div><div class="value" style="top:178px">20</div>
  <div class="progress" style="top:217px"><i style="width:20%"></i></div><div class="value" style="top:217px">29</div>
  <div class="footer"></div><div class="footer-url">www.webaddress.com</div><div class="page-no">8</div>
</div>

<!-- Closing slide -->
<div class="slide col-l row5">
  <svg class="bg" width="543" height="305" viewBox="0 0 543 305">
    <defs><linearGradient id="faded2" x1="0" y1="0" x2="1" y2="1"><stop offset="0" stop-color="#dcdcdc"/><stop offset="1" stop-color="#f1f1f1"/></linearGradient></defs>
    <rect width="543" height="305" fill="url(#faded2)" role="img" aria-label="Faded photo of a desk with a laptop and papers"/>
    <polygon points="0,0 543,0 543,42 271.5,115 0,42" fill="var(--blue)"/>
    <polygon points="0,42 271.5,115 543,42 543,54 271.5,127 0,54" fill="var(--green)"/>
    <polygon points="0,305 543,305 543,232 271.5,170 0,232" fill="var(--blue)"/>
    <polygon points="0,220 271.5,158 543,220 543,232 271.5,170 0,232" fill="var(--green)"/>
  </svg>
  <div class="main-title" style="top:35px;font-size:24px">THANK YOU</div>
  <div class="brand-disc" style="left:217px;top:100px;width:108px;height:108px">Lantern<br>Quorix</div>
  <div class="main-title" style="top:225px;font-size:16px">CONTACT US</div>
  <div class="contact-bar">
    <span><svg width="7" height="9" viewBox="0 0 7 9"><path d="M3.5 0a3.5 3.5 0 0 0-3.5 3.5C0 6 3.5 9 3.5 9S7 6 7 3.5A3.5 3.5 0 0 0 3.5 0z" fill="#fff"/></svg>Address Goes Here</span>
    <span><svg width="8" height="8" viewBox="0 0 8 8"><path d="M1 0h2l1 2-1 1a5 5 0 0 0 2 2l1-1 2 1v2c0 1-1 1-1 1A7 7 0 0 1 0 1S0 0 1 0z" fill="#fff"/></svg>Phone No. Goes Here</span>
    <span><svg width="9" height="7" viewBox="0 0 9 7"><rect width="9" height="7" fill="#fff"/><path d="M0 0l4.5 4L9 0" stroke="var(--blue)" fill="none"/></svg>Email Goes Here</span>
    <span><svg width="8" height="8" viewBox="0 0 8 8"><circle cx="4" cy="4" r="3.4" fill="none" stroke="#fff"/><path d="M.6 4h6.8M4 .6c-2 2-2 4.8 0 6.8M4 .6c2 2 2 4.8 0 6.8" stroke="#fff" stroke-width=".7" fill="none"/></svg>Web Address Goes Here</span>
  </div>
</div>

<div class="brand-mark">Lantern<br>Quorix</div>

</body>
</html>
```